Plum Stride Buisiness card

needing a Business card for our company - Plum Stride.
Plum stride is co owned by Nell and Dermot Wardrop (Husband and Wife)
Services Plum Stride provides include:
Dietetic/nutrition Consultations, weight loss coaching programs, personal and group training, post injury rehab, health and nutrition presentations and Health Retreats.
Nell:
Accredited Practicing Dietitian & Personal trainer
Dermot:
Personal trainer, rehab trainer & Strength and conditioning coach
At this stage the business cards will be made just for Nell.
She has a training studio in Armadale and Dietetics private practice in Richmond.
Mobile services are also available (i.e. meet at house or local cafe)

We need the card to look smart, modern and combine both nutrition and training.
We already have a logo which I will attach.
I was initial thinking i black background but am open to suggestions.

Target Market(s)

Health concious, People with money,

Industry/Entity Type

Nutrition

Contact Information for Business Card

Plum Stride
Nell Wardrop
M: 0431907265
E: plumstride@postwren.com
W: www.plumstride.com.au
Address:
Dietetics: Level 1, 88 Tolley Street
Hollin VIC 3128
Training: Private Studio, behind 517 Merrow St
BRACKLEY, VIC, 3146

Requirements
Must have
• Must have logo (see attached) please not the one we use is the top left (blue and green)
please note attachment is top left (green and blue)

needs to be clear to read - the font needs to be clear and sharp and the background cannot be too busy.eg funny patterns.
Could I please see a card with a line for 'appointment time/date:' possibly on the back. Would like to see what this looks like.
Nell Wardrop's Profile (side of card) must include "Accredited Practicing Dietitian" and "Personal Trainer."
I like when the services plum stride provide are in dot form.
Nice to have
• would like the card to be 2 sides
first side:
Plum stride logo - Large
services plum stride provides: Dietetic/nutrition Consultations, weight loss coaching programs, personal and group training, post injury rehab, health and nutrition presentations and Health Retreats.
web address
second side:
smaller logo
Details for Nell:
Accredited Practicing Dietitian
Personal Trainer
Contact Details:
M: 0431907265
E: plumstride@postwren.com
Address:
Hollin VIC 3128
BRACKLEY, VIC, 3146
Should not have
• Dietetic + nutrition consultations
Should say dietetic/nutrition consultations (first letter of words in capitals please)
Please write phone number as 0431 907 265
Not: 04 31 907265
- note numbers as 4, 3, 3.

```html
<!DOCTYPE html>
<html lang="en">
<head>
<meta charset="utf-8">
<title>Plum Stride – Business Card</title>
<link href="https://fonts.googleapis.com/css2?family=Didact+Gothic&display=swap" rel="stylesheet">
<style>
  :root {
    --page: #3b3b3d;
    --card: #1f1e20;
    --green: #7bb52d;
    --orange: #f08021;
    --white: #f2f2f2;
    --grey: #cfcfcf;
  }
  * { box-sizing: border-box; margin: 0; padding: 0; }
  html, body {
    width: 1200px; height: 901px; overflow: hidden;
    background: var(--page);
    font-family: "Didact Gothic", "Century Gothic", sans-serif;
  }
  .card {
    position: absolute; left: 280px; width: 640px; height: 391px;
    background: var(--card); border-radius: 18px; overflow: hidden;
    box-shadow: 0 10px 30px rgba(0,0,0,.45);
  }
  .card--front { top: 30px; }
  .card--back { top: 471px; }

  /* brand lockup */
  .brand { position: absolute; display: flex; align-items: center; gap: 16px; }
  .brand__dot { border-radius: 50%; background: var(--green); flex: none; }
  .brand__name { color: var(--green); line-height: 1; letter-spacing: -1px; white-space: nowrap; }
  .tagline { position: absolute; color: var(--white); white-space: nowrap; }

  .card--front .brand { left: 48px; top: 52px; }
  .card--front .brand__dot { width: 64px; height: 64px; }
  .card--front .brand__name { font-size: 66px; }
  .card--front .tagline { left: 176px; top: 132px; font-size: 19px; }

  .services {
    position: absolute; left: 56px; top: 192px; width: 560px;
    display: grid; grid-template-columns: 1fr 1.1fr; column-gap: 20px; row-gap: 10px;
    list-style: none; color: var(--white); font-size: 15px; white-space: nowrap;
  }
  .services li::before { content: "•"; color: var(--orange); margin-right: 8px; }

  .web-band {
    position: absolute; left: 0; right: 0; bottom: 0; height: 62px;
    background: var(--green); display: flex; align-items: center; justify-content: center;
    color: var(--white); font-size: 17px; letter-spacing: 9px; text-transform: uppercase;
  }

  .card--back .brand { left: 36px; top: 268px; gap: 10px; }
  .card--back .brand__dot { width: 32px; height: 32px; }
  .card--back .brand__name { font-size: 36px; }
  .card--back .tagline { left: 78px; top: 316px; font-size: 13px; }

  .profile { position: absolute; left: 330px; top: 42px; color: var(--white); font-size: 16px; line-height: 1.3; }
  .profile__name { color: var(--green); font-size: 20px; letter-spacing: 1px; text-transform: uppercase; font-weight: 400; }
  .contact { margin-top: 26px; }
  .contact__row { display: flex; gap: 10px; }
  .contact__label { color: var(--orange); width: 14px; }
  .location { margin-top: 22px; display: flex; gap: 10px; }
  .location + .location { margin-top: 8px; }
  .location svg { flex: none; margin-top: 2px; }
  .location__title { text-transform: uppercase; font-size: 17px; }
  .location--dietetics .location__title { color: var(--green); }
  .location--training .location__title { color: var(--orange); }
  .location__address { color: var(--grey); font-size: 15px; white-space: nowrap; }
</style>
</head>
<body>

<section class="card card--front" aria-label="Card front">
  <div class="brand">
    <span class="brand__dot"></span>
    <span class="brand__name">Plum Stride</span>
  </div>
  <p class="tagline">“Fuel it, then move it!”</p>

  <ul class="services">
    <li>Dietetic/Nutrition Consultations</li>
    <li>Post Injury Rehab</li>
    <li>Weight Loss Coaching Programs</li>
    <li>Health and Nutrition Presentations</li>
    <li>Personal and Group Training</li>
    <li>Health Retreats</li>
  </ul>

  <div class="web-band">www.plumstride.com.au</div>
</section>

<section class="card card--back" aria-label="Card back">
  <div class="profile">
    <h1 class="profile__name">Nell Wardrop</h1>
    <p>Accredited Practicing Dietitian</p>
    <p>Personal Trainer</p>

    <div class="contact">
      <p class="contact__row"><span class="contact__label">M</span><span>0431 907 265</span></p>
      <p class="contact__row"><span class="contact__label">E</span><span>plumstride@postwren.com</span></p>
    </div>

    <div class="location location--dietetics">
      <svg width="16" height="20" viewBox="0 0 16 20" aria-hidden="true"><path d="M8 0a8 8 0 0 0-8 8c0 6 8 12 8 12s8-6 8-12a8 8 0 0 0-8-8zm0 11a3 3 0 1 1 0-6 3 3 0 0 1 0 6z" fill="var(--green)"/></svg>
      <div>
        <p class="location__title">Dietetics:</p>
        <p class="location__address">Level 1, 88 Tolley Street<br>Hollin VIC 3128</p>
      </div>
    </div>
    <div class="location location--training">
      <svg width="16" height="20" viewBox="0 0 16 20" aria-hidden="true"><path d="M8 0a8 8 0 0 0-8 8c0 6 8 12 8 12s8-6 8-12a8 8 0 0 0-8-8zm0 11a3 3 0 1 1 0-6 3 3 0 0 1 0 6z" fill="var(--orange)"/></svg>
      <div>
        <p class="location__title">Training:</p>
        <p class="location__address">Private Studio, behind 517 Merrow St<br>BRACKLEY, VIC, 3146</p>
      </div>
    </div>
  </div>

  <div class="brand">
    <span class="brand__dot"></span>
    <span class="brand__name">Plum Stride</span>
  </div>
  <p class="tagline">“Fuel it, then move it!”</p>
</section>

</body>
</html>
```